I need a business card design for my new clinic (SPORTS MEDICINE OF KNEE). I am orthopedist, expert in sports surgery, especially knee surgery. I prefer, as colors, the colors of my logo (green, black and white). I already have my logo and should appear on my card. It's good to see my site to have ideas (www.drlucianovarela.com)
It needs contain:
my name: Dr. Luciano Varela
my registration: CRM 584-902
my specialty: Cirurgia do Joelho / Esporte
my address: Centro Executivo - Pinheiral Plaza
Av. Doutor Augusto Brandão Cunha, 2740 sala 0836
Jd. Ipanema - Ribeirão Preto - SP
my phone number: Tel (16) 8245-3908
my clinic phone: (16) 3670-4851
my e-mail: drlucianovarela@mailbox-exemplo.com
my site: www.drlucianovarela.com

Target Market(s)

futures patients

Industry/Entity Type

Clinic

Requirements
Nice to have
• letters not overfilled
straight lines, with few curves

```html
<!DOCTYPE html>
<html lang="pt-BR">
<head>
<meta charset="utf-8">
<title>Dr. Luciano Varela – Business Card</title>
<link rel="stylesheet" href="https://fonts.googleapis.com/css2?family=Crimson+Text:wght@400;600;700&display=swap">
<style>
  :root {
    --backdrop: #a7a8aa;
    --paper: #ffffff;
    --ink: #1d1d1b;
    --muted: #7a7a7a;
    --green: #2f9a62;
    --green-light: #80c79d;
    --green-text: #3aa86d;
    --shadow: rgba(0,0,0,0.35);
  }
  * { margin: 0; padding: 0; box-sizing: border-box; }
  html, body { width: 800px; height: 1200px; overflow: hidden; }
  body {
    background: var(--backdrop);
    font-family: "Crimson Text", Georgia, serif;
    color: var(--ink);
    position: relative;
  }
  .card {
    position: absolute;
    left: 62px;
    width: 680px;
    height: 437px;
    background: var(--paper);
    box-shadow: 6px 6px 8px var(--shadow);
    overflow: hidden;
  }
  .card--front { top: 80px; }
  .card--back { top: 601px; }
  .card__wave { position: absolute; left: 0; top: 0; width: 680px; height: 437px; }
  .abs { position: absolute; white-space: nowrap; }

  .doctor-name { left: 372px; top: 32px; font-size: 21px; font-weight: 700; }
  .specialty {
    left: 372px; top: 60px; font-size: 15px; color: var(--muted);
    font-variant: small-caps; letter-spacing: 0.6px; font-weight: 600;
  }
  .registration { left: 372px; top: 80px; font-size: 14px; color: var(--muted); letter-spacing: 0.4px; }
  .address { left: 372px; top: 121px; font-size: 15.5px; line-height: 19.5px; font-style: normal; }
  .contacts { left: 372px; top: 206px; font-size: 15.5px; list-style: none; }
  .contacts li { height: 27.5px; display: flex; align-items: center; }
  .contacts .label {
    width: 24px; font-size: 10px; font-weight: 700; color: var(--green-text);
    padding-top: 3px;
  }
  .brand-square {
    position: absolute; left: 42px; top: 250px; width: 50px; height: 50px;
    background: var(--green);
  }
  .brand-name {
    left: 108px; top: 253px; font-size: 32px; font-weight: 600;
    color: var(--ink); line-height: 44px;
  }

  .appointment-title {
    left: 37px; top: 34px; font-size: 19px; font-weight: 600;
    color: var(--green-text); letter-spacing: 0.3px;
  }
  .weekdays { left: 37px; top: 70px; display: flex; font-size: 12px; font-weight: 700; letter-spacing: 0.5px; }
  .weekdays span { width: 70px; display: flex; align-items: center; gap: 8px; }
  .checkbox { width: 11px; height: 11px; border: 2px solid var(--ink); display: inline-block; }
  .field { left: 37px; font-size: 15.5px; display: flex; align-items: baseline; gap: 8px; }
  .field--date { top: 104px; }
  .field--time { top: 140px; }
  .field .line { width: 178px; border-bottom: 1px dotted var(--ink); height: 1px; }
  .reschedule { left: 37px; top: 296px; font-size: 15.5px; }
  .back-square {
    position: absolute; left: 565px; top: 287px; width: 68px; height: 64px;
    background: var(--green);
  }
</style>
</head>
<body>

<section class="card card--front">
  <svg class="card__wave" viewBox="0 0 680 437" aria-hidden="true">
    <path d="M0,338 C160,318 300,392 480,392 C570,392 630,364 680,352 L680,437 L0,437 Z" fill="var(--green-light)"/>
    <path d="M0,356 C160,338 300,410 480,408 C570,407 630,380 680,368 L680,437 L0,437 Z" fill="var(--green)"/>
  </svg>

  <div class="brand-square"></div>
  <div class="abs brand-name">Varela</div>

  <h1 class="abs doctor-name">Dr. Luciano Varela</h1>
  <p class="abs specialty">Cirurgia do Joelho / Esporte</p>
  <p class="abs registration">CRM 584-902</p>

  <address class="abs address">
    Centro Executivo - Pinheiral Plaza<br>
    Av. Doutor Augusto Brandão Cunha<br>
    2740 sala 0836 Jd. Ipanema<br>
    Ribeirão Preto - SP
  </address>

  <ul class="abs contacts">
    <li><span class="label">M</span>(16) 8245-3908</li>
    <li><span class="label">T</span>(16) 3670-4851</li>
    <li><span class="label">E</span>drlucianovarela@mailbox-exemplo.com</li>
    <li><span class="label">W</span>www.drlucianovarela.com</li>
  </ul>
</section>

<section class="card card--back">
  <svg class="card__wave" viewBox="0 0 680 437" aria-hidden="true">
    <path d="M0,338 C160,318 300,392 480,392 C570,392 630,364 680,352 L680,437 L0,437 Z" fill="var(--green-light)"/>
    <path d="M0,356 C160,338 300,410 480,408 C570,407 630,380 680,368 L680,437 L0,437 Z" fill="var(--green)"/>
  </svg>

  <h2 class="abs appointment-title">YOUR NEXT APPOINTMENT</h2>
  <div class="abs weekdays">
    <span>MON <i class="checkbox"></i></span>
    <span>TUE <i class="checkbox"></i></span>
    <span>WED <i class="checkbox"></i></span>
    <span>THU <i class="checkbox"></i></span>
    <span>FRI <i class="checkbox"></i></span>
  </div>
  <div class="abs field field--date">Date: <span class="line"></span></div>
  <div class="abs field field--time">Time: <span class="line"></span></div>

  <p class="abs reschedule">Please call (16) 3670-4851 to re-schedule or cancel</p>
  <div class="back-square"></div>
</section>

</body>
</html>
```